Dynamic Website Design For Dynamic Speaker and Business Coach!

Professional Website Design for a for a Professional Business coach, Business trainer, and Speaker.

Note: This is for design only. No coding required. We want to see your ideas for a great website! This will be a FUN design and not boring like others you may work on.

Please let your creative ideas flow. We have given you a ton of info along with videos to help you understand what we are after, however we WANT your creativity to shine through in your designs!

We are a professional company that has run hundreds of crowdsourced projects on multiple platforms. If you participate in this contest (we hope you do) you can expect great video feedback, consistent feedback, and also our guarantee that if we know your website design will not be what we are looking for we will notify you so you don’t waste your time if there is no chance of you winning.

We respect and recognize this is how you make your living and we will not play games. We look forward to an awesome contest and awesome website designs.

Design Brief:

We are looking for a fresh and fun new design for

http://www.brightpath-advisory.net

This individual (Dana Holloway) teaches and trains corporations and businesses in the fields of leadership, sales, communication, business operations etc. Additionally this business teaches and mentors business professionals in a small group level or 1 on 1.

The website needs to convey trust, professionalism, and affluent, while at the same time having some personality!

This business operates on 3 core principles that we would like to see incorporated into the logo if it is a good fit. The 3 principals are:

Focus
Accountability
Results

Here is a video to help explain what we like about the current site and what we don’t like:
http://clipvault.example/t/QwpLmr82kTnb

As you can see the website is geared towards business professionals. Please look over the website to learn what they do. Obviously this is not a good website so we need your help.

We want a website that is professional-looking, has personality and is geared more towards promoting Dana Holloway, the owner of Summit Path Advisory as a Speaker and Business Consultant. The more you can incorporate clean, professional and fun personality elements into the design, the better off you are at winning.

Here are some examples of other sites in their business that have some things we like:

http://velvetcompass.com Please watch video to learn what we like and don’t like:
http://clipvault.example/t/NrtHq7YpLwc

http://tallpinegrowth.com Please watch video to learn what we like and don’t like:
http://clipvault.example/t/J8vDkrWa

http://www.marthaquince.com Please watch video to learn what we like and don’t like:
http://clipvault.example/t/Pz3mx9Rb2Kq

http://www.vantix7.com Please watch video to learn what we like and don’t like:
http://clipvault.example/t/7Gwe4sNhydv

NOTE: We do not want to copy anything outright. We want to learn, model and take their ideas and make them better. We also want to be flexible and take what we like along with your creativity to make an amazing design.

Here is what we are looking for in more specific terms:

Colors: We like the darker blue (not the light blue like the site) and also a burnt orange. I’ve attached her Logo so you can get an idea and feel for the colors.

When looking at colors please know that the current site and look is NOT what we are going for. We are going for a clean and professional look but also a look that is BOLD, FUN, and Vibrant (hence the colors).

Menu: Horizontal. We like bold and easy to read menu items. Don’t make it small and cluttered.

Site Structure: Clean and easy to navigate. We have a lot of content to display so we need a clean structure that breaks up the text and content areas.
Images: Please pull images from the current site. We can always replace the images of course, but if you show them “their own stuff” in the new design you will be closer to winning because it will feel more like “them”

Look and Feel: Professional. Fun. High-End. Business-like. This website needs to convey that Dana Holloway and Summit Path Advisory are professional. That Dana Holloway is a sought-after Speaker and Business Consultant who knows what she is talking about; can be serious when she needs to be, but also likes to have fun with her clients. This site must convey that!

Content Areas: It is a safe bet that if it is on the current site we need it on the new site. So don’t drop anything as it makes it hard to “cut content”.

What we don't want: We do not want clutter, boring, or templates or themes. We don’t want too cartoony, too cute, or too fancy… Be creative!

Out of respect to professional designers who really are working hard to win if you do not follow this brief, you submit worn out themes, templates, or boring designs you will be eliminated. We are offering great prize money for this so we expect great visual designs.
Updates

Project Deadline Extended
Reason: Our client is out of town, and waiting to hear feedback from them. So, in the meantime, we wanted to keep the project going to see what else you designers can come up with. As soon as we hear back from our client, we will pass along the info. Thanks!

Target Market(s)

Target Audience is entrepreneurs and business professionals alike. This is all business to business stuff.

This person teaches and trains startups and billion dollar companies. The common thread is that they are all businesses and companies who need help in various areas including sales, communication, business operations, etc.

Industry/Entity Type

Business

Font styles to use
Sans Serif

Requirements
Must have
• Brief is very detailed. Please review
Nice to have
Should not have

```html
<!DOCTYPE html>
<html lang="en">
<head>
<meta charset="utf-8">
<title>Summit Path Advisory – Albuquerque Business Coaching</title>
<link href="https://fonts.googleapis.com/css2?family=Ubuntu:wght@400;500;700&family=Open+Sans:wght@400;600;700&display=swap" rel="stylesheet">
<style>
:root{
  --blue:#1f5e8e;
  --blue-dark:#174a72;
  --navy:#0f3f63;
  --heading:#17679a;
  --gold:#f0b41c;
  --gold-dark:#d99f12;
  --orange:#e8731f;
  --text:#5d5d5d;
  --white:#ffffff;
  --grey-top:#d9d9d9;
  --grey-mid:#f3f3f3;
}
*{margin:0;padding:0;box-sizing:border-box}
html,body{width:759px;height:1200px;overflow:hidden;background:var(--white)}
body{position:relative;font-family:'Open Sans',sans-serif;color:var(--text)}
.abs{position:absolute}
.ubuntu{font-family:'Ubuntu',sans-serif}

/* header */
.brand{left:12px;top:14px;display:flex;align-items:center;gap:8px}
.brand-dot{width:30px;height:30px;border-radius:50%;background:var(--orange)}
.brand-name{font-family:'Ubuntu',sans-serif;font-weight:700;font-size:19px;line-height:20px;color:var(--blue);width:140px}
.phone{left:446px;top:12px;font-family:'Ubuntu',sans-serif;font-weight:700;font-size:20px;color:var(--blue);display:flex;align-items:center;gap:6px}
.search{left:470px;top:47px;width:148px;height:18px;border:1px solid #bbb;font-size:8px;padding:3px 5px;color:#555;background:#fff}
.sharing{left:645px;top:12px;font-size:9px;font-style:italic;color:#666}
.social{display:flex;gap:5px}
.social span{width:25px;height:25px;border-radius:4px;background:var(--blue)}
.social.header{left:647px;top:37px}

/* nav */
.nav{left:0;top:79px;width:759px;height:24px;background:var(--blue);display:flex}
.nav a{font-family:'Ubuntu',sans-serif;font-weight:500;font-size:9.5px;color:#fff;text-decoration:none;padding:0 11.5px;line-height:24px;border-right:1px solid rgba(255,255,255,.15)}
.nav a.active{background:var(--navy)}

/* hero */
.hero{left:0;top:103px;width:759px;height:237px;background:linear-gradient(#d8d8d8,#f4f4f4 40%,#f4f4f4 80%,#e4e4e4)}
.hero-title{left:40px;top:150px;width:302px;text-align:center;font-family:'Ubuntu',sans-serif;font-size:22.5px;line-height:26px;color:var(--heading)}
.hero-sub{left:81px;top:215px;width:220px;height:27px;border-top:1px solid #aaa;border-bottom:1px solid #aaa;text-align:center;font-family:'Ubuntu',sans-serif;font-size:14px;line-height:25px;color:#555}
.btn{top:258px;height:35px;font-family:'Ubuntu',sans-serif;font-weight:700;font-size:10.5px;display:flex;align-items:center;justify-content:center;border-radius:2px}
.btn-tv{left:37px;width:160px;background:var(--navy);color:#fff}
.btn-videos{left:204px;width:136px;background:var(--gold);color:var(--blue-dark)}
.video{left:362px;top:127px;width:345px;height:194px;background:linear-gradient(135deg,#3e7fbf,#2a63a2 60%,#1d4d86)}
.video-figure{right:18px;top:0;width:105px;height:194px;background:linear-gradient(#5a4a42,#232833)}
.video-text{left:8px;top:22px;width:230px;text-align:center;font-family:Georgia,serif;font-size:31px;line-height:32px;color:#fff}
.video-share{right:6px;top:6px;width:20px;height:20px;background:rgba(0,0,0,.45);border-radius:3px}
.video-bar{left:6px;bottom:6px;width:333px;height:20px;background:rgba(0,0,0,.55);border-radius:2px}
.video-bar .track{left:50px;top:9px;width:255px;height:2px;background:#999}
.video-bar .play{left:0;top:0;width:36px;height:20px;background:#111}

/* sign-up band */
.signup{left:0;top:340px;width:759px;height:131px;background:var(--gold);text-align:center;color:#fff}
.signup h2{font-family:'Ubuntu',sans-serif;font-weight:400;font-size:19.5px;margin-top:16px}
.signup .free{font-size:12px;margin-top:1px}
.signup .free b{color:var(--blue-dark);font-weight:700}
.signup .report{font-size:12px;margin-top:8px}
.signup .report b{font-weight:600}
.field{top:435px;height:20px;background:#fff;border:1px solid #e3e3e3;font-size:8px;padding:4px 6px;color:#555}
.submit{left:556px;top:435px;width:76px;height:20px;background:#3b3b3b;color:#fff;font-size:8px;font-weight:700;text-align:center;line-height:20px}

/* sidebar */
.portrait{left:50px;top:500px;width:159px;height:239px;background:linear-gradient(#8a8f94,#5a7a8c 55%,#2b2b2b)}
.name-band{left:50px;top:694px;width:159px;height:45px;background:rgba(240,180,28,.92);color:#fff;font-weight:700;font-size:12px;text-align:center;line-height:45px}
.testimonial{left:50px;top:750px;width:159px;height:247px;border:1px solid #bbb;padding:8px}
.testimonial h3{font-family:'Ubuntu',sans-serif;font-size:14px;color:var(--blue);border-bottom:1px solid #bbb;padding-bottom:6px;display:flex;gap:6px}
.testimonial h3 i{color:var(--gold);font-style:normal;font-family:Georgia,serif}
.testimonial p{font-size:8.6px;line-height:15.2px;margin-top:10px}
.testimonial .cite{font-size:9.5px;line-height:13px;color:#333;margin-top:4px}
.badges{left:66px;top:1010px;display:flex;gap:15px}
.badges span{width:38px;height:37px;border-radius:50%;background:#2d5f8e}
.badges span.sq{border-radius:0;background:#c9744a}

/* main copy */
.copy{left:235px;width:480px;font-size:9px;line-height:15.2px}
.copy h2{font-family:'Ubuntu',sans-serif;font-weight:500;font-size:14.3px;line-height:17px;color:var(--heading)}
.ticks{list-style:none}
.ticks li{display:flex;align-items:center;gap:6px;height:18.2px;font-size:9.3px}
.ticks svg{flex:none}

/* footer */
.footer{left:0;top:1105px;width:759px;height:95px;background:var(--blue)}
.contact-bar{left:34px;top:1070px;width:686px;height:59px;background:var(--gold);display:flex;align-items:center;color:#fff;font-size:17px}
.contact-bar .cell{height:59px;display:flex;align-items:center;gap:10px;padding-left:20px}
.contact-bar .mail{background:var(--gold-dark);width:251px}
.contact-bar .tel{width:203px}
.social.footer-s{margin-left:32px}
.footer-links{left:0;top:1148px;width:759px;text-align:center;font-size:9.5px;font-weight:700;color:#fff}
.copyright{left:0;top:1165px;width:759px;text-align:center;font-size:8.8px;color:#fff}
</style>
</head>
<body>

<header>
  <div class="abs brand">
    <span class="brand-dot"></span>
    <span class="brand-name">Summit Path Advisory</span>
  </div>
  <div class="abs phone">
    <svg width="15" height="15" viewBox="0 0 24 24"><path fill="#222" d="M6.6 10.8a15 15 0 0 0 6.6 6.6l2.2-2.2c.3-.3.7-.4 1-.2 1.1.4 2.3.6 3.6.6.6 0 1 .4 1 1V20c0 .6-.4 1-1 1A17 17 0 0 1 3 4c0-.6.4-1 1-1h3.5c.6 0 1 .4 1 1 0 1.3.2 2.5.6 3.6.1.3 0 .7-.2 1z"/></svg>
    (505)555-0182
  </div>
  <div class="abs search">Search</div>
  <div class="abs sharing">Sharing is caring!</div>
  <div class="abs social header"><span></span><span></span><span></span></div>
</header>

<nav class="abs nav">
  <a class="active">Home</a><a>Passion</a><a>Who We Are</a><a>Speaker</a><a>Free Videos</a><a>Web TV Show</a><a>Testimonials</a><a>Corwin Learning</a><a>Blog</a><a>Contact</a>
</nav>

<section class="abs hero"></section>
<h1 class="abs hero-title" style="font-weight:400">Albuquerque Business Coaching and Consulting</h1>
<div class="abs hero-sub">What do you want more of?</div>
<div class="abs btn btn-tv">UNPLUGGED WEB TV SHOW</div>
<div class="abs btn btn-videos">FREE INSIDER VIDEOS</div>

<div class="abs video">
  <div class="abs video-figure" role="img" aria-label="Dana Holloway speaking to camera in the intro video"></div>
  <div class="abs video-text">Do You Need More Focus, Accountability &amp; Results?</div>
  <div class="abs video-share"></div>
  <div class="abs video-bar">
    <div class="abs play"><svg width="36" height="20"><path d="M14 5l10 5-10 5z" fill="#fff"/></svg></div>
    <div class="abs track"></div>
  </div>
</div>

<section class="abs signup">
  <h2>Change your thinking, change your results!</h2>
  <p class="free">Sign up for my <b>FREE</b> report</p>
  <p class="report"><b>"Have Fun While Making Sales"</b> and make more money this month!</p>
</section>
<div class="abs field" style="left:117px;width:142px">Name</div>
<div class="abs field" style="left:262px;width:142px">Phone</div>
<div class="abs field" style="left:408px;width:142px">Email</div>
<div class="abs submit">SUBMIT</div>

<aside>
  <div class="abs portrait" role="img" aria-label="Portrait photo of Dana Holloway"></div>
  <div class="abs name-band">DANA HOLLOWAY</div>
  <div class="abs testimonial">
    <h3><i>“</i>Testimonial</h3>
    <p>“Dana is an enthusiastic and engaging instructor who strives at every opportunity to provide a worthwhile and purposeful workshop to her audience. She is fun, easy to work with, and full of great information! A real asset to any organization looking for professional training.”</p>
    <p class="cite">Lena Marsh -<br>Former Advanced Sales Training Manager</p>
  </div>
  <div class="abs badges"><span></span><span></span><span class="sq"></span></div>
</aside>

<svg width="0" height="0" style="position:absolute">
  <symbol id="tick" viewBox="0 0 14 14"><rect x="1" y="2" width="10" height="10" rx="2" fill="none" stroke="#555" stroke-width="1.4"/><path d="M3.5 6.5l2.5 2.5 6-7" fill="none" stroke="#555" stroke-width="1.8"/></symbol>
</svg>

<main>
  <p class="abs copy" style="top:502px">Are you searching to bridge the gap between where you are and where you want to be?<br>As you face greater pressure to “move the needle” on your company’s productivity and bottom line profitability, how prepared are you to step in and shine as the leader?<br>We specialize in guiding leaders to become easier to follow.&nbsp; You’re in the Right Place.</p>
  <h2 class="abs copy" style="top:568px;font-family:'Ubuntu',sans-serif;font-weight:500;font-size:14.3px;color:var(--heading)">Albuquerque Business Coach: Focus, Accountability, &amp; Results</h2>
  <ul class="abs copy ticks" style="top:588px">
    <li><svg width="12" height="12"><use href="#tick"/></svg>Development Of An Operational Plan That Links All Departments</li>
    <li><svg width="12" height="12"><use href="#tick"/></svg>Implementation And Monitoring Individual And Departmental Plans</li>
    <li><svg width="12" height="12"><use href="#tick"/></svg>Diagnosing Employee Training Needs</li>
    <li><svg width="12" height="12"><use href="#tick"/></svg>Delivering The Training To Develop Leaders And Staff</li>
    <li><svg width="12" height="12"><use href="#tick"/></svg>Coach Leaders, Individuals And Teams</li>
  </ul>
  <p class="abs copy" style="top:685px">Whether you’re leading a company, or are an employee, all of us have a role to play in contributing to the profit and the future of the company.</p>
  <h2 class="abs copy" style="top:725px;font-family:'Ubuntu',sans-serif;font-weight:500;font-size:14.3px;color:var(--heading)">Your organization expects you to deliver value by delivering results.</h2>
  <p class="abs copy" style="top:741px;left:238px">At Summit Path Advisory, we know as a company or as individuals, clarity of the direction captured in an annual plan that is monitored monthly is one of the surest, quickest and most profitable ways of getting ahead in these challenging times.</p>
  <p class="abs copy" style="top:801px;left:238px">What is the missing link in your business?&nbsp; What are you searching for?&nbsp; Email me today, conversation is complimentary to investigate where we start building&nbsp; the business you envision for tomorrow.</p>
  <h2 class="abs copy" style="top:843px;left:237px;font-family:'Ubuntu',sans-serif;font-weight:500;font-size:14.3px;color:var(--heading)">Summit Path Advisory has delivered on our promise.<br>Our clients learn to:</h2>
  <ul class="abs copy ticks" style="top:880px;left:237px">
    <li><svg width="12" height="12"><use href="#tick"/></svg>Establish new patterns of productivity for the business</li>
    <li><svg width="12" height="12"><use href="#tick"/></svg>Clarification of future goals, targets and benchmarks</li>
    <li><svg width="12" height="12"><use href="#tick"/></svg>Implement actionable steps around short, medium and long-term goals</li>
    <li><svg width="12" height="12"><use href="#tick"/></svg>Identify roadblocks and disempowering habits</li>
    <li><svg width="12" height="12"><use href="#tick"/></svg>Create a repeatable process that delivers results</li>
    <li><svg width="12" height="12"><use href="#tick"/></svg>Transform burned out employees or leaders into fired-up employees</li>
  </ul>
  <p class="abs copy" style="top:998px;left:238px">With over 25 years of experience in a variety of industries, we know the daily attitudes, habits and goals for successful companies begin with a plan.&nbsp; By training employees where needed and coaching to clear expectations writes success stories daily as the plan unfolds over the course of the year.</p>
</main>

<footer>
  <div class="abs footer"></div>
  <div class="abs contact-bar">
    <div class="cell tel">
      <svg width="18" height="16" viewBox="0 0 24 20"><path fill="#fff" d="M2 6c0-3 4-5 10-5s10 2 10 5v2h-6V6H8v2H2zM5 10h14l2 9H3zM12 12a3 3 0 1 0 0 6 3 3 0 0 0 0-6z"/></svg>
      (505)555-0182
    </div>
    <div class="cell mail">
      <svg width="20" height="15" viewBox="0 0 20 15"><rect width="20" height="15" rx="1" fill="#fff"/><path d="M1 1l9 7 9-7" fill="none" stroke="#d99f12" stroke-width="1.6"/></svg>
      <span style="font-size:14.5px">dana@summitpathadvisory.net</span>
    </div>
    <div class="social footer-s"><span></span><span></span><span></span></div>
  </div>
  <div class="abs footer-links">Passion | Who We Are | Speaker | Free Videos | Web TV Show | Testimonials | Corwin Learning | Blog | Contact</div>
  <div class="abs copyright">©2014 Summit Path Advisory</div>
</footer>

</body>
</html>
```